TEK Logistics - Banner 2.5' x 8' for 20+ locations

Need a banner designed that will pop. This banner will be displayed at over 20 of our transportation facilities. Goal is for the banner to grab the attention of employees, contractors and clients and help reinforce our mission and core values. Designed needs to include TEK Logo, our core values and mission statement. Red and Black are the main company colors and we need to stay within that theme and color pallet. Attached is a previous version that was too basic and boring. Willing to consider a design that excludes the mission statement.

Gathering more feedback

```html
<!DOCTYPE html>
<html lang="en">
<head>
<meta charset="utf-8">
<title>TEK Logistics – Mission &amp; Core Values Banner</title>
<link href="https://fonts.googleapis.com/css2?family=Arimo:wght@400;700&display=swap" rel="stylesheet">
<style>
  :root{
    --page:#fdfdfd;
    --ink-dark:#1c1d1e;
    --ink-mid:#2c2d2f;
    --ink-light:#4b4c4e;
    --brand-red:#d42a2a;
    --text-white:#ffffff;
    --text-soft:#f0f0f0;
  }
  *{box-sizing:border-box;margin:0;padding:0}
  html,body{width:1200px;height:1200px;overflow:hidden;background:var(--page)}
  body{position:relative;font-family:"Arimo",Arial,sans-serif}

  .banner{
    position:absolute;left:62px;top:431px;width:1083px;height:345px;
    background:linear-gradient(100deg,var(--ink-dark) 0%,var(--ink-mid) 45%,var(--ink-light) 100%);
    box-shadow:0 1px 4px rgba(0,0,0,.25);
    overflow:hidden;color:var(--text-white);
  }

  .container-visual{
    position:absolute;right:0;top:0;width:420px;height:100%;
    background:linear-gradient(145deg,#5a5b5d 0%,#7a7b7d 25%,#9e2424 45%,#6e6f71 60%,#b52a2a 78%,#5c5d5f 100%);
    -webkit-mask-image:linear-gradient(90deg,transparent 0%,#000 40%);
    mask-image:linear-gradient(90deg,transparent 0%,#000 40%);
  }

  .brand{
    position:absolute;left:46px;top:70px;width:150px;
  }
  .brand-name{
    display:block;font-weight:700;font-size:28px;line-height:32px;color:var(--brand-red);
  }

  .mission{
    position:absolute;left:222px;top:73px;width:468px;
    font-weight:700;font-size:18.3px;line-height:25px;color:var(--text-white);
  }

  .values-title{
    position:absolute;left:47px;top:186px;
    font-weight:700;font-size:19px;color:var(--brand-red);
  }

  .values-list{position:absolute;list-style:none;font-size:16px;line-height:24.4px;color:var(--text-soft);letter-spacing:.3px}
  .values-list li{position:relative;padding-left:14px}
  .values-list li::before{
    content:"";position:absolute;left:0;top:10px;width:5px;height:5px;border-radius:50%;background:var(--brand-red);
  }
  .values-left{left:47px;top:220px}
  .values-right{left:431px;top:218px}

  .values-divider{
    position:absolute;left:387px;top:222px;width:1px;height:73px;background:var(--brand-red);
  }
</style>
</head>
<body>
  <section class="banner">
    <div class="container-visual" role="img" aria-label="Aerial view of stacked red and grey shipping containers"></div>

    <div class="brand">
      <span class="brand-name">TEK<br>Logistics</span>
    </div>

    <p class="mission">Provide the best customer experience while creating an environment of growth and opportunity for our customers, employees, and service providers.</p>

    <h2 class="values-title">Core Values:</h2>

    <ul class="values-list values-left">
      <li>Do the right things for the right reasons</li>
      <li>Pursue growth and development</li>
      <li>Build a positive team atmosphere</li>
    </ul>

    <div class="values-divider"></div>

    <ul class="values-list values-right">
      <li>Deliver WOW through service</li>
      <li>Do everything Safely</li>
      <li>Have Fun</li>
    </ul>
  </section>
</body>
</html>
```